Polish brewery needs BEER LABEL design for WEDDINGS

We need beer label design for weddings. Our brewery is located on South of Poland and it is called Zakład Wrzos [PL]/Heather Works [ENG]. We feel strong connection to mountains and we use water from the mountain in our vicinity.
Regarding beer style it is India Pale Ale so beer is bitter and aromatic because of high addition of hops. Label design has to be modern and simple. We would prefer bright and cream colors.
We need to have opportunity to edit data which are on the label so we will need to get appropriate files.
In attached files you can find all details. If any additional information will be required please do not hesitate and contact with me.

Target Market(s)

Weddings

Font styles to use
Sans Serif
Script

Colors
ffffff

Requirements
Must have
• Information listed in documents in attached files
Nice to have
• Some nice graphics
Bright and cream colors.
Should not have
• -

```html
<!DOCTYPE html>
<html lang="pl">
<head>
<meta charset="utf-8">
<title>Etykieta weselna IPA – Zakład Wrzos</title>
<link href="https://fonts.googleapis.com/css2?family=Arimo:wght@400;700&family=Kaushan+Script&display=swap" rel="stylesheet">
<style>
  :root {
    --ink: #111;
    --frame: #1d4a5c;
    --blue: #1f74bb;
    --blue-soft: #9cc9ea;
    --paper: #ffffff;
    --leaf: #8fae93;
    --copper: #d98a35;
  }
  * { box-sizing: border-box; margin: 0; padding: 0; }
  html, body { width: 1200px; height: 533px; overflow: hidden; background: var(--paper); }
  body { font-family: "Arimo", Arial, sans-serif; color: var(--ink); }
  .label { position: relative; width: 1200px; height: 533px; background: var(--paper); }
  .frame-outer { position: absolute; left: 8px; top: 8px; width: 1185px; height: 517px; border: 3px solid var(--frame); }
  .frame-inner { position: absolute; left: 14px; top: 14px; width: 1173px; height: 505px; border: 1px solid var(--frame); }
  .corner { position: absolute; width: 46px; height: 46px; background: linear-gradient(135deg, var(--frame), #5f8ea0); opacity: .85; }
  .corner.tl { left: 12px; top: 12px; border-bottom-right-radius: 40px; }
  .corner.tr { right: 7px; top: 12px; border-bottom-left-radius: 40px; }
  .corner.bl { left: 12px; bottom: 8px; border-top-right-radius: 40px; }
  .corner.br { right: 7px; bottom: 8px; border-top-left-radius: 40px; }

  .panel { position: absolute; top: 47px; width: 332px; height: 440px; border: 2px dashed var(--blue); }
  .panel-info { left: 44px; padding: 8px 10px 0 9px; }
  .panel-story { left: 820px; padding: 8px 9px 0 8px; }

  .info-block { position: relative; }
  .info-title { font-size: 20px; font-weight: 700; line-height: 24px; }
  .info-title .light { font-weight: 400; }
  .info-text { font-size: 18px; line-height: 23px; }
  .rule-blue { height: 3px; background: var(--blue); }
  .rule-thin { height: 1px; background: var(--ink); }
  .ingredients { height: 79px; padding-top: 4px; }
  .best-before { height: 95px; padding-top: 6px; }
  .storage { height: 80px; padding-top: 2px; line-height: 28px; }
  .volume { height: 54px; padding-top: 2px; }
  .producer { display: flex; justify-content: space-between; padding-top: 5px; }
  .producer .info-text { line-height: 22.5px; }
  .brand-name { align-self: flex-end; margin-bottom: 4px; font-size: 16px; font-weight: 700; line-height: 18px; text-align: center; color: var(--ink); }

  .story { font-size: 18px; line-height: 22.6px; text-align: justify; height: 173px; }
  .stats { padding: 9px 0 0 5px; height: 178px; }
  .stat { display: flex; align-items: center; height: 33.5px; font-size: 20px; }
  .stat-name { width: 93px; }
  .stat-value { color: var(--blue); font-size: 20px; }
  .icons { display: flex; gap: 6px; }
  .icon { width: 14px; height: 22px; border-radius: 6px; background: var(--blue); }
  .icon.hop { width: 20px; border-radius: 10px 10px 10px 10px / 8px 8px 12px 12px; }
  .icon.grain { width: 10px; }
  .icon.off { background: var(--blue-soft); }
  .icon.drop { width: 28px; height: 30px; border-radius: 50% 50% 50% 50% / 40% 40% 60% 60%; background: linear-gradient(180deg, #7fb9e3, var(--frame)); }
  .social { padding: 5px 0 0 5px; font-size: 18px; line-height: 22.6px; }
  .social b { font-weight: 700; }

  .centre { position: absolute; left: 420px; top: 20px; width: 360px; height: 500px; }
  .wreath { position: absolute; left: 78px; top: 4px; width: 211px; height: 200px; border-radius: 50%;
    background: radial-gradient(circle, #ffffff 45%, #eef3ea 62%, #d9e4d5 74%, rgba(243,210,170,.5) 86%, rgba(255,255,255,0) 100%); }
  .couple { position: absolute; left: 0; top: 56px; width: 100%; text-align: center; font-family: "Kaushan Script", cursive; font-size: 30px; line-height: 34px; }
  .couple .heart { display: block; margin: 2px auto 3px; width: 22px; height: 20px; }
  .ornament { position: absolute; background: linear-gradient(180deg, #444, #111); opacity: .85; border-radius: 20px; }
  .flourish-top { left: 148px; top: 210px; width: 64px; height: 40px; }
  .flourish-bottom { left: 148px; top: 448px; width: 64px; height: 44px; }
  .divider { position: absolute; left: 9px; width: 345px; height: 10px; }
  .date { position: absolute; left: 0; top: 256px; width: 100%; text-align: center; font-family: "Kaushan Script", cursive; font-size: 34px; }
  .arrows { position: absolute; left: 109px; width: 142px; height: 10px; }
</style>
</head>
<body>
<main class="label">
  <div class="frame-outer"></div>
  <div class="frame-inner"></div>
  <div class="corner tl" role="img" aria-label="Ozdobny narożnik ramki"></div>
  <div class="corner tr" role="img" aria-label="Ozdobny narożnik ramki"></div>
  <div class="corner bl" role="img" aria-label="Ozdobny narożnik ramki"></div>
  <div class="corner br" role="img" aria-label="Ozdobny narożnik ramki"></div>

  <section class="panel panel-info">
    <div class="info-block ingredients">
      <h2 class="info-title">Składniki:</h2>
      <p class="info-text">woda, słód jęczmienny, chmiel, liście limonki, drożdże.</p>
    </div>
    <div class="rule-blue"></div>
    <div class="info-block best-before">
      <h2 class="info-title">Najlepiej spożyć przed<span class="light">:</span></h2>
      <p class="info-text">Data stanowi numer partii</p>
    </div>
    <div class="rule-thin"></div>
    <div class="info-block storage">
      <p class="info-text" style="line-height:28px">Przechowywać w suchym i chłodnym miejscu</p>
    </div>
    <div class="rule-thin"></div>
    <div class="info-block volume">
      <h2 class="info-title">Objętość butelki:</h2>
      <p class="info-text">330ml</p>
    </div>
    <div class="rule-blue"></div>
    <div class="producer">
      <p class="info-text">Zakład Wrzos<br>34-512 Wrzosowa Dolina<br>Browar Pod Halą<br>Leśna 48, Halne<br>34-640</p>
      <p class="brand-name">ZAKŁAD<br>WRZOS</p>
    </div>
  </section>

  <section class="centre">
    <div class="wreath" role="img" aria-label="Wianek z liści eukaliptusa i miedziana geometryczna rama"></div>
    <h1 class="couple">Hanna
      <svg class="heart" viewBox="0 0 22 20" aria-hidden="true"><path d="M11 19 C4 13 1 10 1 6 C1 3 3 1 6 1 C8 1 10 2 11 4 C12 2 14 1 16 1 C19 1 21 3 21 6 C21 10 18 13 11 19Z" fill="#111"/></svg>
      Tomasz</h1>
    <div class="ornament flourish-top" role="img" aria-label="Ozdobny ornament"></div>
    <svg class="divider" style="top:248px" viewBox="0 0 345 10" aria-hidden="true">
      <line x1="10" y1="5" x2="335" y2="5" stroke="#111" stroke-width="2.5"/>
      <ellipse cx="6" cy="5" rx="5" ry="3.5" fill="none" stroke="#111" stroke-width="1.8"/>
      <ellipse cx="339" cy="5" rx="5" ry="3.5" fill="none" stroke="#111" stroke-width="1.8"/>
    </svg>
    <p class="date">15.3.20</p>
    <div class="ornament arrows" style="top:302px" role="img" aria-label="Ozdobnik ze strzałkami"></div>
    <div class="ornament arrows" style="top:369px" role="img" aria-label="Ozdobnik ze strzałkami"></div>
    <svg class="divider" style="top:441px" viewBox="0 0 345 10" aria-hidden="true">
      <line x1="10" y1="5" x2="335" y2="5" stroke="#111" stroke-width="2.5"/>
      <ellipse cx="6" cy="5" rx="5" ry="3.5" fill="none" stroke="#111" stroke-width="1.8"/>
      <ellipse cx="339" cy="5" rx="5" ry="3.5" fill="none" stroke="#111" stroke-width="1.8"/>
    </svg>
    <div class="ornament flourish-bottom" role="img" aria-label="Ozdobny ornament"></div>
  </section>

  <section class="panel panel-story">
    <p class="story">Trzymasz w ręku naszą autorską IPA do produkcji której wykorzystujemy wodę wypływającą z samego serca Beskidu Wysokiego - Babiej Góry. IPA lubi chmiele i goryczkę, ale żeby nie było nudno postanowiliśmy ją wzbogacić limonką.</p>
    <div class="rule-blue"></div>
    <div class="stats">
      <div class="stat"><span class="stat-name">ALK</span><span class="stat-value">5,5%</span></div>
      <div class="stat"><span class="stat-name">IBU</span>
        <span class="icons" role="img" aria-label="Goryczka: 2 z 3 szyszek chmielu"><i class="icon hop"></i><i class="icon hop"></i><i class="icon hop off"></i></span></div>
      <div class="stat"><span class="stat-name">EBC</span>
        <span class="icons" role="img" aria-label="Barwa: 1 z 3 kłosów"><i class="icon grain"></i><i class="icon grain off"></i><i class="icon grain off"></i></span></div>
      <div class="stat"><span class="stat-name">EXT</span><span class="stat-value">14%</span></div>
      <div class="stat"><span class="stat-name">WATER</span><span class="icon drop" role="img" aria-label="Kropla górskiej wody"></span></div>
    </div>
    <div class="rule-blue"></div>
    <p class="social"><b>FB</b> - zakladwrzos<br><b>INSTA</b> - zakladwrzos.pl<br><b>WEBSITE</b> - www.zakladwrzos.pl</p>
  </section>
</main>
</body>
</html>
```